Client Centric Brochure for Investment Advisory Firm

We need a client centric firm brochure that not only spotlights the services we provide as a wealth and investment management firm but also the value our expertise and expierience brings. We would like see designs that use this particular color green (RGB-0,92,51) and variations. Shouldn't be limited to this color however and are open to other color schemes Looking for something clean and consise. The final design should communicate financial safety, growth and reaching investment goals. Attached are rudimentary designs we have created, our company logo, and other source material. You can also visit our website www.birchmontwealth.com for more inspiration.

Target Market(s)

Age Range - 35-65, Gender - 70% male, 30% female, Those looking to secure their financial future through wealth management and investing.

Industry/Entity Type

Investment

Font styles to use
Serif
Sans Serif

Colors
00a990

Requirements
Must have
• Project must have some of the information that was provided in the source documents. It must exhibit the client centric nature we are trying to exude.

```html
<!DOCTYPE html>
<html lang="en">
<head>
<meta charset="utf-8">
<title>Birchmont Wealth – Brochure Cover</title>
<link rel="stylesheet" href="https://fonts.googleapis.com/css2?family=Cinzel:wght@500&family=Tenor+Sans&display=swap">
<style>
  :root {
    --page-bg: #e9eae9;
    --paper: #f7f7f8;
    --brand-green: #005c33;
    --green-mid: #2f6b4c;
    --green-soft: #4f8f6e;
    --text-dark: #2b2b2b;
    --text-light: #eef5f0;
    --photo-dark: #2c2f2c;
    --photo-mid: #5d6a52;
    --photo-green: #8fae4a;
  }
  * { margin: 0; padding: 0; box-sizing: border-box; }
  html, body {
    width: 1200px; height: 789px; overflow: hidden;
    background: var(--page-bg);
  }
  .cover {
    position: absolute; left: 320px; top: 24px;
    width: 560px; height: 741px;
    background: var(--paper);
    box-shadow: 0 4px 18px rgba(0,0,0,.18);
    overflow: hidden;
  }
  .cover-photo {
    position: absolute; left: 0; top: 115px; width: 560px; height: 520px;
    background: linear-gradient(180deg, #8e948e 0%, var(--photo-mid) 35%, var(--photo-green) 55%, #6d6b4a 68%, var(--photo-dark) 80%, #1f211f 100%);
  }
  .cover-shapes { position: absolute; inset: 0; width: 560px; height: 741px; }
  .brand {
    position: absolute; left: 54px; top: 44px;
    display: flex; align-items: center; gap: 14px;
  }
  .brand-square {
    width: 30px; height: 30px; background: var(--brand-green);
  }
  .brand-name {
    font-family: "Cinzel", serif; font-weight: 500;
    font-size: 30px; color: var(--text-dark); letter-spacing: .5px;
  }
  .tagline {
    position: absolute; left: 58px; top: 638px;
    font-family: "Tenor Sans", sans-serif; font-size: 22px; line-height: 1.2;
    color: var(--text-light); transform: rotate(-2.2deg); transform-origin: left center;
    display: flex; align-items: center; gap: 12px; white-space: nowrap;
  }
  .tagline-dot {
    width: 6px; height: 6px; border-radius: 50%; background: #8dc3a3;
  }
  .website {
    position: absolute; left: 0; width: 560px; top: 702px;
    display: flex; justify-content: center; align-items: center; gap: 10px;
    transform: rotate(-2.2deg);
    font-family: "Cinzel", serif; font-size: 15px; letter-spacing: 1px;
    color: var(--text-light);
  }
</style>
</head>
<body>
  <article class="cover">
    <div class="cover-photo" role="img" aria-label="Photograph of an underground train station platform with benches, overhead signs and a colourful green mosaic wall"></div>

    <svg class="cover-shapes" viewBox="0 0 560 741" aria-hidden="true">
      <polygon class="facet" points="330,160 440,60 560,60 560,180 470,290" fill="rgba(0,92,51,.55)"/>
      <polygon class="facet" points="280,260 410,130 540,260 410,390" fill="rgba(60,140,100,.45)"/>
      <polygon class="facet" points="340,420 470,290 560,380 560,460 470,550" fill="rgba(0,92,51,.5)"/>
      <polygon class="facet" points="310,490 420,390 530,495 440,590" fill="rgba(140,190,165,.42)"/>
      <polygon class="facet" points="450,580 510,520 560,560 560,630 490,630" fill="rgba(0,92,51,.45)"/>
      <polygon class="band-light" points="0,628 440,611 490,648 560,645 560,741 0,741" fill="var(--green-soft)"/>
      <polygon class="band-dark" points="0,692 560,670 560,741 0,741" fill="var(--green-mid)"/>
      <polyline class="band-rule" points="0,622 440,605 490,642 560,639" fill="none" stroke="#f4f6f4" stroke-width="3"/>
    </svg>

    <div class="brand">
      <span class="brand-square"></span>
      <span class="brand-name">Birchmont Wealth</span>
    </div>

    <p class="tagline">
      <span>Simple</span><span class="tagline-dot"></span>
      <span>Efficient</span><span class="tagline-dot"></span>
      <span>Innovative</span>
    </p>

    <p class="website">
      <svg width="16" height="16" viewBox="0 0 16 16" aria-hidden="true">
        <g fill="none" stroke="#eef5f0" stroke-width="1.2">
          <circle cx="8" cy="8" r="7"/>
          <ellipse cx="8" cy="8" rx="3" ry="7"/>
          <line x1="1" y1="8" x2="15" y2="8"/>
        </g>
      </svg>
      <span>WWW.BIRCHMONTWEALTH.COM</span>
    </p>
  </article>
</body>
</html>
```